KRM

I just wrote a novel that I plan on marketing through my website. Please use my uploaded files to add on to your design... The name of the book is "Lanterns under the frost".

Industry/Entity Type

Marketing

Font styles to use
Serif
Sans Serif

Colors

Designer to choose colors to be used in the design.

```html
<!DOCTYPE html>
<html lang="en">
<head>
<meta charset="utf-8">
<title>KRM presents "Lanterns Under the Frost"</title>
<link rel="stylesheet" href="https://fonts.googleapis.com/css2?family=Arimo:ital,wght@0,400;0,700;1,400&family=Open+Sans:wght@400;600&display=swap">
<style>
  :root {
    --navy: #201c70;
    --red: #d9232a;
    --gold: #f5b800;
    --ink: #4f4f55;
    --muted: #9a9aa2;
    --soft: #c9c9dc;
    --rule: #d6d6d6;
    --white: #ffffff;
    --link-blue: #5a5ad6;
  }
  * { box-sizing: border-box; margin: 0; padding: 0; }
  html, body { width: 1200px; height: 1000px; overflow: hidden; background: var(--white); }
  body { position: relative; font-family: "Arimo", Arial, sans-serif; color: var(--ink); }
  .abs { position: absolute; }

  /* Header */
  .brand-mark {
    left: 571px; top: 50px; width: 115px; height: 115px; border-radius: 50%;
    background: #111; display: flex; align-items: center; justify-content: center;
    color: var(--white); font-size: 30px; font-weight: 700; letter-spacing: 1px;
  }
  .presents { left: 0; width: 1248px; top: 174px; text-align: center; font-size: 11px; color: #666; }
  .book-title { left: 0; width: 1232px; top: 211px; text-align: center; font-size: 26px; color: var(--red); font-weight: 400; letter-spacing: .3px; }
  .title-rule { left: 405px; top: 260px; width: 436px; height: 1px; background: var(--rule); }
  .byline { left: 0; width: 1256px; top: 279px; text-align: center; font-size: 14px; color: var(--ink); }
  .byline .author-name { color: var(--navy); }

  /* Feature band */
  .feature-band { left: 0; top: 328px; width: 1200px; height: 352px; background: var(--navy); }
  .author-portrait {
    left: 210px; top: 278px; width: 104px; height: 104px; border-radius: 50%;
    border: 4px solid var(--white);
    background: radial-gradient(circle at 50% 40%, #c9a58c 0%, #8a6b58 45%, #cfe0ee 75%, #a9c4dc 100%);
  }

  .chapter-nav { left: 258px; top: 428px; width: 140px; height: 140px; }
  .chapter-nav .track { position: absolute; left: 5px; top: 41px; width: 1px; height: 87px; background: var(--white); }
  .chapter-nav .item { position: absolute; left: 0; height: 14px; display: flex; align-items: center; font-size: 12.5px; color: var(--soft); }
  .chapter-nav .dot { width: 11px; height: 11px; border-radius: 50%; background: var(--white); margin-right: 14px; position: relative; z-index: 1; }
  .chapter-nav .item.is-current { color: var(--gold); }
  .chapter-nav .item.is-current .dot { background: var(--gold); }

  .cover-art {
    left: 431px; top: 430px; width: 148px; height: 193px;
    background: linear-gradient(180deg, #f2ece4 0%, #c8362f 30%, #6b5a78 60%, #2d2440 85%, #8c1d1d 100%);
  }

  .intro-heading { left: 618px; top: 429px; font-size: 14px; font-weight: 700; color: var(--white); }
  .intro-text { left: 620px; top: 467px; font-size: 12.2px; line-height: 15.2px; color: var(--white); white-space: nowrap; }
  .read-more { left: 618px; top: 558px; font-size: 9.5px; font-weight: 700; color: var(--gold); text-decoration: underline; }
  .buy-link { left: 617px; top: 596px; display: flex; align-items: center; }
  .buy-link .cart-badge { width: 28px; height: 28px; border-radius: 50%; background: var(--white); display: flex; align-items: center; justify-content: center; }
  .buy-link .label { margin-left: 11px; font-size: 10px; font-weight: 700; color: #8d8db0; letter-spacing: .2px; }

  /* Order & testimonial */
  .banner-art {
    left: 209px; top: 753px; width: 181px; height: 102px;
    background: linear-gradient(180deg, #5a3b2a 0%, #c9262c 25%, #d8a36b 55%, #c9262c 70%, #4a3a3a 100%);
  }
  .order-heading { left: 418px; top: 750px; font-size: 14px; font-weight: 400; color: var(--muted); }
  .order-heading strong { color: var(--gold); font-weight: 700; }
  .order-text { left: 418px; top: 787px; width: 180px; font-family: "Open Sans", Arial, sans-serif; font-size: 8.6px; line-height: 12.5px; color: #8a8a8a; }
  .pay-option {
    top: 829px; height: 24px; border: 1px solid #d0d0d0; border-radius: 3px;
    background: linear-gradient(#ffffff, #eeeeee);
    display: flex; align-items: center; justify-content: center;
    font-size: 7px; font-weight: 700; color: #3b3b5a;
  }
  .pay-option.first { left: 419px; width: 37px; }
  .pay-option.second { left: 468px; width: 37px; font-size: 6px; }
  .column-rule { left: 620px; top: 748px; width: 1px; height: 117px; background: var(--rule); }

  .quote-badge { left: 828px; top: 748px; }
  .testimonial-text { left: 675px; top: 782px; font-size: 11.2px; line-height: 15.3px; font-style: italic; color: #a3a3a8; white-space: nowrap; }
  .testimonial-source { left: 675px; top: 848px; font-size: 11px; font-style: italic; color: var(--link-blue); }

  /* Footer */
  .site-footer { left: 0; top: 941px; width: 1200px; height: 59px; background: var(--navy); }
  .site-footer p { position: absolute; left: 209px; top: 28px; font-family: "Open Sans", Arial, sans-serif; font-size: 8.6px; color: #e6e6f0; }
</style>
</head>
<body>
  <header>
    <div class="abs brand-mark">KRM</div>
    <p class="abs presents">PRESENT'S</p>
    <h1 class="abs book-title">"LANTERNS UNDER THE FROST"</h1>
    <div class="abs title-rule"></div>
    <p class="abs byline">WRITTEN BY - <span class="author-name">JULIAN M. CARROW</span></p>
  </header>

  <section class="abs feature-band" aria-label="Book introduction"></section>
  <div class="abs author-portrait" role="img" aria-label="Portrait photo of the author"></div>

  <nav class="abs chapter-nav">
    <div class="track"></div>
    <div class="item is-current" style="top:0"><span class="dot"></span>Home</div>
    <div class="item" style="top:34px"><span class="dot"></span>About Book</div>
    <div class="item" style="top:62px"><span class="dot"></span>About Author</div>
    <div class="item" style="top:92px"><span class="dot"></span>Testimonial</div>
    <div class="item" style="top:121px"><span class="dot"></span>Contact</div>
  </nav>

  <div class="abs cover-art" role="img" aria-label="Front cover of the novel Lanterns Under the Frost"></div>

  <h2 class="abs intro-heading">INTRODUCTION</h2>
  <p class="abs intro-text">Lorem Ipsum is simply dummy text of the printing and typesetting industry.<br>Lorem Ipsum has been the industry's standard dummy text ever since the<br>1500s, when an unknown printer took a galley of type and scrambled it to<br>make a type specimen book.</p>
  <a class="abs read-more">READ MORE</a>
  <a class="abs buy-link">
    <span class="cart-badge">
      <svg width="14" height="13" viewBox="0 0 14 13" fill="none" stroke="#c0394a" stroke-width="1.2" stroke-linecap="round" stroke-linejoin="round">
        <path d="M1 1.5h2l1.6 7h6.8l1.4-5H4"/>
        <circle cx="5.5" cy="11" r="1"/>
        <circle cx="10.5" cy="11" r="1"/>
      </svg>
    </span>
    <span class="label">BUY THIS BOOK</span>
  </a>

  <section aria-label="Order and testimonial">
    <div class="abs banner-art" role="img" aria-label="Promotional banner for Lanterns Under the Frost"></div>
    <h3 class="abs order-heading">ORDER THIS BOOK <strong>NOW!</strong></h3>
    <p class="abs order-text">Lorem Ipsum is simply dummy text of the printing and typesetting industry</p>
    <span class="abs pay-option first">Purselo</span>
    <span class="abs pay-option second">Marketnook</span>
    <div class="abs column-rule"></div>

    <svg class="abs quote-badge" width="22" height="22" viewBox="0 0 22 22">
      <circle cx="11" cy="11" r="9.5" fill="none" stroke="#777" stroke-width="2"/>
      <path d="M6.5 13.5c0-3 1.2-4.6 3.4-5.2v1.3c-1 .4-1.5 1.1-1.6 2h1.6v3H6.5zM11.8 13.5c0-3 1.2-4.6 3.4-5.2v1.3c-1 .4-1.5 1.1-1.6 2h1.6v3h-3.4z" fill="#777"/>
    </svg>
    <blockquote class="abs testimonial-text">Lorem Ipsum is simply dummy text of the printing and typesetting indus-<br>try. Lorem Ipsum has been the industry's standard dummy text ever since<br>the 1500s</blockquote>
    <p class="abs testimonial-source">- by Northwind Studio</p>
  </section>

  <footer class="abs site-footer">
    <p>Copyright All Right Reserved 2014.</p>
  </footer>
</body>
</html>
```